Law Firm Website

We are looking to update our old, tired and very flat website. We have someone who will code and host the site but we need some design inspiration. The website will consist of no more than 2/3 pages, possibly with pop-ups for information. We already have all the blurb. We would like something distinctive, clean and eye-catching, using the purple and white theme that we already use on our firm stationery. Examples uploaded. Current website URL is www.dunmorewillett.example.

Industry/Entity Type

Law Firm

```html
<!DOCTYPE html>
<html lang="en">
<head>
<meta charset="utf-8">
<title>Dunmore + Willett Solicitors</title>
<link rel="stylesheet" href="https://fonts.googleapis.com/css2?family=Open+Sans:ital,wght@0,300;0,400;0,600;1,400&display=swap">
<style>
:root{
  --purple:#534f96;
  --purple-light:#b9b6e0;
  --ink:#111;
  --logo:#26352f;
  --red:#ee3a37;
  --grey:#bdbdbd;
  --white:#fff;
}
*{margin:0;padding:0;box-sizing:border-box}
html,body{width:1200px;height:1179px;overflow:hidden;background:var(--white)}
body{position:relative;font-family:Arial,Helvetica,sans-serif;color:var(--ink)}
.abs{position:absolute}

/* header */
.brand{left:186px;top:18px;font-family:"Open Sans",sans-serif;font-weight:600;color:var(--logo);line-height:1}
.brand-name{font-size:33px;letter-spacing:-.5px;white-space:nowrap}
.brand-sub{font-size:16px;margin:6px 0 0 60px}
.address{right:188px;top:28px;text-align:right;font-family:"Open Sans",sans-serif;font-size:11px;line-height:15.5px;color:#222;font-style:normal}

/* nav */
.nav{left:0;top:94px;width:1200px;height:41px;background:var(--purple)}
.nav ul{list-style:none;position:absolute;left:173px;top:0;display:flex;height:41px}
.nav li{font-family:"Open Sans",sans-serif;font-size:14.5px;color:var(--white);padding:0 13px;line-height:41px;text-transform:uppercase;white-space:nowrap}
.nav li.active{background:#000;padding:0 19px}
.search{left:876px;top:106px;width:136px;height:17px;background:var(--white);border:1px solid #ccc;font-size:10px;color:#aaa;padding:2px 6px}
.search svg{position:absolute;right:6px;top:3px}

/* hero */
.hero{left:0;top:135px;width:1200px;height:292px;background:linear-gradient(90deg,#6a6a6a 0%,#3a3a3a 30%,#1c1c1c 55%,#2a2a2a 80%,#4a4a4a 100%)}
.hero-text{right:188px;top:202px;text-align:right;color:var(--white);font-family:"Open Sans",sans-serif;line-height:1;white-space:nowrap}
.hero-title{font-size:27px}
.hero-lede{font-size:24px;line-height:28.5px;margin-top:4px}
.pill{font-family:"Open Sans",sans-serif;color:var(--white);border-radius:9px;text-align:center;font-size:9.5px;white-space:nowrap}
.hero-cta{left:901px;top:314px;width:111px;height:17px;line-height:17px;background:var(--purple)}

/* content */
.section-title{font-family:"Open Sans",sans-serif;font-size:21px;font-weight:400;display:flex;align-items:flex-end;white-space:nowrap}
.section-title span{flex:1;border-bottom:1px dashed #555;margin:0 0 6px 4px}
.profile-title{left:186px;top:488px;width:604px}
.lead{left:187px;top:527px;width:610px;font-size:16.3px;line-height:18.5px}
.body-copy{left:187px;top:569px;width:610px;font-size:12px;line-height:18px;color:#222}
.learn-more{left:722px;top:666px;width:71px;height:16px;line-height:16px;background:var(--red)}
.areas-title{left:186px;top:700px;width:615px}
.areas{left:187px;top:751px;width:614px;height:207px;background:var(--purple)}
.area-list{position:absolute;top:38px;list-style:none;width:140px}
.area-list li{font-family:"Open Sans",sans-serif;font-size:10.5px;color:var(--white);height:21px;line-height:19px;white-space:nowrap;border-bottom:1px dotted var(--purple-light)}
.area-list li:last-child{border-bottom:none}
.area-list li::before{content:"›";margin-right:4px}

/* sidebar */
.sidebar{left:825px;top:464px;width:187px;height:494px;background:#000;color:var(--white)}
.side-title{position:absolute;left:16px;font-family:"Open Sans",sans-serif;font-weight:300;font-size:22px;line-height:27px;white-space:nowrap}
.field{position:absolute;left:17px;width:154px;background:var(--white);font-size:10px;color:#888}
.field .ico{position:absolute;left:0;top:0;width:23px;height:100%;background:var(--grey);display:flex;align-items:flex-start;justify-content:center;padding-top:6px}
.field .ico.red{background:var(--red)}
.field b{font-weight:normal;position:absolute;left:27px;top:9px}
.submit{position:absolute;left:17px;top:275px;width:154px;height:29px;background:var(--red);font-family:"Open Sans",sans-serif;font-weight:600;font-size:13.5px;text-align:center;line-height:29px}
.rule{position:absolute;left:15px;top:368px;width:152px;height:1px;background:var(--white)}
.rule::after{content:"";position:absolute;left:20px;top:0;border:4px solid transparent;border-top-color:var(--white)}
.quote{position:absolute;left:15px;top:389px;width:150px;font-family:"Open Sans",sans-serif;font-size:10.3px;line-height:12.7px}
.quote-by{position:absolute;left:15px;top:455px;font-family:"Open Sans",sans-serif;font-style:italic;font-size:12px;color:#999}

/* footer */
.footer{left:0;top:1045px;width:1200px;height:134px;background:var(--purple)}
.footer-badge{left:568px;top:1014px;width:64px;height:64px;border-radius:50%;background:var(--white)}
.footer-links{left:0;top:1094px;width:1200px;text-align:center;font-family:"Open Sans",sans-serif;font-size:11.5px;color:var(--purple-light);white-space:nowrap}
.footer-links i{font-style:normal;margin:0 6px}
.footer-meta{left:450px;top:1116px;height:30px;display:flex;align-items:center;font-family:"Open Sans",sans-serif;font-size:10.5px;color:#d6d4ef;white-space:nowrap}
.footer-meta .divider{width:1px;height:30px;background:#d6d4ef;margin:0 10px}
.dot{display:inline-block;width:11px;height:11px;border-radius:50%;background:#d6d4ef;margin-right:8px}
</style>
</head>
<body>

<header>
  <div class="abs brand">
    <div class="brand-name">Dunmore + Willett</div>
    <div class="brand-sub">Solicitors</div>
  </div>
  <address class="abs address">
    No. 12, 4 Larkhall Rise<br>Clapham London SW4 7QE<br>Tel.: +0300 555 0142
  </address>
</header>

<nav class="abs nav">
  <ul>
    <li>Home</li>
    <li class="active">Area of Expertise</li>
    <li>Edward Dunmore</li>
    <li>Simon Willett</li>
    <li>Contact</li>
  </ul>
</nav>
<div class="abs search">Search
  <svg width="8" height="8" viewBox="0 0 8 8"><circle cx="3" cy="3" r="2.2" fill="none" stroke="#888" stroke-width="1.2"/><path d="M4.6 4.6 7.5 7.5" stroke="#888" stroke-width="1.3"/></svg>
</div>

<section class="abs hero" role="img" aria-label="Black and white photograph of solicitors in business suits standing side by side"></section>
<div class="abs hero-text">
  <div class="hero-title">Dunmore + Willett Solicitors</div>
  <div class="hero-lede">Lorem ipsum dolor sit amet,<br>consectetur adipisicing elit,</div>
</div>
<div class="abs pill hero-cta">Fee Consultation</div>

<main>
  <h2 class="abs section-title profile-title">Firm Profile<span></span></h2>
  <p class="abs lead">Lorem ipsum dolor sit amet, consectetur adipiscing elit. In fermentum dolor non augue pretium egestas. Donec sem eros, tincidunt congue ut, posuere sit amet est.</p>
  <p class="abs body-copy">Vivamus scelerisque viverra odio sit amet laoreet. Ut nec neque non justo rutrum tempor lobortis ante. Dolor aliquam sagittis Lorem ipsum dolor sit amet, consectetur adipiscing elit. In fermentum dolor non augue pretium egestas. Donec sem eros, tincidunt at congue ut, posuere sit amet est. Vivamus scelerisque viverra odio sit amet laoreet. In fermentum dolor non augue pretium egestas. Donec sem eros, dolor sit amet, consectetur adipiscing elit. In fermentum dolor non augue pretium egestas. Donec sem eros</p>
  <div class="abs pill learn-more">Learn More</div>

  <h2 class="abs section-title areas-title">Our Practice Areas<span></span></h2>
  <div class="abs areas">
    <ul class="area-list" style="left:31px">
      <li>Lorem Ipsum Donor Amet</li><li>Sed do eiusmod tempor</li><li>Eiusmod tempor incidi</li><li>amet Consecteur</li><li>donor sit amet</li><li>Adipisicing elit sed to</li>
    </ul>
    <ul class="area-list" style="left:227px">
      <li>Lorem Ipsum Donor Amet</li><li>Sed do eiusmod tempor</li><li>Eiusmod tempor incidi</li><li>amet Consecteur</li><li>donor sit amet</li><li>Adipisicing elit sed to</li>
    </ul>
    <ul class="area-list" style="left:415px">
      <li>Lorem Ipsum Donor Amet</li><li>Sed do eiusmod tempor</li><li>Eiusmod tempor incidi</li><li>amet Consecteur</li><li>donor sit amet</li><li>Adipisicing elit sed to</li>
    </ul>
  </div>
</main>

<aside class="abs sidebar">
  <h3 class="side-title" style="top:29px">Free<br>Consultation</h3>
  <div class="field" style="top:95px;height:29px"><div class="ico red">
    <svg width="13" height="15" viewBox="0 0 13 15"><circle cx="6.5" cy="4" r="3.5" fill="#fff"/><path d="M0 15c0-5 3-7 6.5-7S13 10 13 15z" fill="#fff"/></svg></div><b>Name</b></div>
  <div class="field" style="top:128px;height:29px"><div class="ico">
    <svg width="15" height="11" viewBox="0 0 15 11"><rect x=".5" y=".5" width="14" height="10" fill="none" stroke="#fff"/><path d="M.5 .5 7.5 6 14.5 .5" fill="none" stroke="#fff"/></svg></div><b>Email</b></div>
  <div class="field" style="top:160px;height:29px"><div class="ico">
    <svg width="10" height="16" viewBox="0 0 10 16"><rect x=".7" y=".7" width="8.6" height="14.6" rx="1.5" fill="none" stroke="#fff" stroke-width="1.4"/><rect x="2.5" y="2.5" width="5" height="9" fill="#fff"/></svg></div><b>Phone</b></div>
  <div class="field" style="top:192px;height:78px"><div class="ico">
    <svg width="14" height="14" viewBox="0 0 14 14"><rect x=".7" y="2.7" width="10.6" height="10.6" fill="none" stroke="#fff" stroke-width="1.4"/><path d="M5 9 13 1" stroke="#fff" stroke-width="2"/></svg></div><b style="top:7px">Comments</b></div>
  <div class="submit">SUBMIT</div>
  <h3 class="side-title" style="top:330px;left:15px">Testimonials</h3>
  <div class="rule"></div>
  <p class="quote">“Lorem ipsum dolor sit amet, consectetur amet adipiscing elit. In fermentum congu adipiscing sit amet dolor sit amet, consectetur ”</p>
  <div class="quote-by">Martin</div>
</aside>

<footer>
  <div class="abs footer"></div>
  <div class="abs footer-badge"></div>
  <div class="abs footer-links">Home<i>-</i>Area of Expertise<i>-</i>Edward Dunmore<i>-</i>Simon Willett<i>-</i>Contact</div>
  <div class="abs footer-meta">
    <span>Call : 0300 555 0142</span>
    <span class="divider"></span>
    <span class="dot"></span><span class="dot"></span>
    <svg width="18" height="12" viewBox="0 0 18 12"><rect x=".5" y=".5" width="17" height="11" fill="none" stroke="#d6d4ef"/><path d="M.5 .5 9 7 17.5 .5" fill="none" stroke="#d6d4ef"/></svg>
    <span class="divider"></span>
    <span>© Copyright 2014</span>
  </div>
</footer>

</body>
</html>
```